Design wireframe of E-commerce website *

We are a European online shoe store located in Sweden. The project is to redesign the first page of our e-commerce website https://velmiro.se/skor
We want to receive creative ideas of what our website could look like while keeping all the functions and flows. The new design should be simple, lean and modern.
Specifications:
We have several guidelines for what we are expecting
- Redesign the frontend of our website first page https://velmiro.se/skor and the child page https://www.velmiro.se/skor/dam
- You need to provide a complete clickable wireframe of the target pages.
- All existing components should be in the new design.
- The pages should include all sections: header, footer, product lists and widgets. The page structure of the site should look as the example: https://www.quistle.co.uk/shoes
- The design must be responsive and Mobile First which can be read from all browsers and different devices.
- You need to have in mind that we really want it to be mobile first, meaning
the mobile view is the most important one
- The new design should reflect our brands essence and come along with the new brandprofiles (fonts, icons...). For example http://brandprofile.quistle.com/, but keep the logo and colour of the existing Velmiro theme.
- The design should be user friendly.
- The design should be simple enough that the pages can be downloaded fast.
- The new design should look fashionable and be able to generating attracting
traffic.
- The text on the child page https://www.velmiro.se/skor/dam should be handled in a better way and make it easier for users to know which page they are looking at. You can see the example at https://www.quistle.co.uk/shoes/women but we are open to your good ideas as well.
- We do not want shelves in the design. Quistle has it, but Velmiro
should not.
- We want to keep the existing responsive sizes for product list which means 2, 4 or 6 pairs of shoes per row.
Practical Information:
We are located in Sweden and have working hours between 9:00 -12:00 (CEST)
Monday - Friday. We have limited capacity to answer every question you have
but will try to get back to you in our working hours as much as we can then
hopefully this can help you get a better understanding of what we are
looking for.
Future Possibilities:We are going to redesign the whole site
of https://www.velmiro.se/skor so the winner
will have the chance to do all the pages in the near future. We are
actively seeking designers for future collaborations on a long-term basis
and it is possible to create a partnership if your work is impressive
enough. *

```html
<!DOCTYPE html>
<html lang="en">
<head>
<meta charset="utf-8">
<title>Velmiro – Shoes</title>
<link href="https://fonts.googleapis.com/css2?family=Roboto:wght@300;400;500;700;900&family=Roboto+Slab:wght@400;700&display=swap" rel="stylesheet">
<style>
:root{
  --red:#c8102e;
  --dark:#1d1d1f;
  --darker:#141416;
  --ink:#222;
  --muted:#777;
  --line:#e2e2e2;
  --panel:#f3f3f3;
  --stage:#ececef;
  --white:#fff;
  --orange:#e9a35a;
}
*{box-sizing:border-box;margin:0;padding:0}
html,body{width:1200px;height:4932px;overflow:hidden}
body{background:var(--stage);font-family:'Roboto',sans-serif;color:var(--ink)}
.page{position:absolute;left:400px;top:250px;width:400px;background:var(--white);box-shadow:0 4px 30px rgba(0,0,0,.08)}
.red{color:var(--red)}
.btn{display:inline-block;font-size:9px;padding:5px 14px;border:1px solid currentColor;letter-spacing:.3px}
.btn-solid{background:var(--red);color:var(--white);border-color:var(--red)}
.btn-outline{color:var(--red);border-color:var(--red);background:var(--white)}
.center{text-align:center}

/* header */
.topbar{height:63px;background:var(--dark);display:flex;align-items:center;justify-content:space-between;padding:0 16px}
.logo{font-weight:900;color:var(--red);font-size:22px;letter-spacing:.3px}
.topbar .icons{display:flex;gap:12px}
.topbar svg{display:block}

/* hero */
.hero{height:548px;background:var(--darker);position:relative;padding:60px 36px 0}
.hero .deal{font-family:'Roboto Slab',serif;color:var(--red);font-size:58px;line-height:1}
.hero .sub{color:var(--white);font-weight:700;font-size:22px;margin:14px 0 18px;letter-spacing:.5px}
.hero .btn{color:var(--white)}
.hero .photo{position:absolute;left:36px;right:36px;bottom:40px;height:220px;background:radial-gradient(ellipse at 50% 60%,#5a3b2c 0%,#3a2a22 40%,var(--darker) 75%)}
.dots{display:flex;justify-content:center;gap:5px;padding:20px 0}
.dots i{width:5px;height:5px;border-radius:50%;background:#bbb}
.dots i.on{background:#555}

/* categories */
.cats{padding:4px 37px 0;display:flex;flex-direction:column;gap:16px}
.cat{height:216px;position:relative;color:var(--white);padding:0 20px;display:flex;flex-direction:column;justify-content:center}
.cat.men{background:linear-gradient(135deg,#8a7a66,#5b4d40)}
.cat.women{background:linear-gradient(135deg,#9a8d8e,#b45a6a)}
.cat.kids{background:linear-gradient(135deg,#8c7f86,#b0506e)}
.cat .off{font-size:12px}
.cat h3{font-size:22px;font-weight:500;margin:4px 0 8px}
.cat .btn{font-size:8px;align-self:flex-start;padding:3px 10px}
.cat.women{align-items:center;text-align:center}
.cat.women .btn{align-self:center}
.cat.kids{align-items:flex-end;text-align:right}
.cat.kids .btn{align-self:flex-end}

/* products */
.popular{padding-top:36px}
.section-title{font-size:30px;font-weight:400;text-align:center}
.tabs{display:flex;justify-content:center;gap:14px;font-size:14px;margin:18px 0 24px}
.tabs span{color:var(--muted)}
.tabs .on{color:var(--red)}
.tabs b{font-weight:300;color:#999}
.grid{display:grid;grid-template-columns:1fr 1fr}
.product{text-align:center;padding-bottom:22px}
.product .shot{height:120px;position:relative;background:linear-gradient(180deg,transparent 42%,var(--orange) 42%,var(--orange) 56%,transparent 56%)}
.product .shot span{position:absolute;left:50%;top:14px;transform:translateX(-50%);width:110px;height:80px;border-radius:40% 50% 30% 30%}
.product .name{font-size:11px;color:#555;margin-top:10px}
.product .price{font-size:11px;color:var(--red);font-weight:700;margin-top:6px}
.product .actions{display:flex;gap:8px;justify-content:center;margin-top:6px}
.product .actions .btn{font-size:7px;padding:2px 14px}
.more{text-align:center;padding:14px 0 28px}

/* banner */
.arrived{height:220px;background:linear-gradient(90deg,#f4f4f4 45%,#dcd6d2);display:flex;align-items:center;padding:0 16px;position:relative}
.arrived h3{font-size:26px;font-weight:500;letter-spacing:.5px}
.arrived p{font-size:8px;font-weight:700;letter-spacing:.5px;margin:2px 0 8px}
.arrived .row{display:flex;gap:6px}
.arrived .row .btn{font-size:7px;padding:3px 12px}
.arrived .photo{position:absolute;right:16px;top:30px;width:170px;height:160px;background:radial-gradient(ellipse,#5b3225 0%,#8a5a46 45%,transparent 72%)}

/* testimonial */
.clients{background:var(--panel);margin:30px 0 0;padding:30px 24px 24px;text-align:center}
.clients h2{font-size:21px;font-weight:500}
.avatar{width:104px;height:104px;border-radius:50%;margin:22px auto 14px;background:linear-gradient(160deg,#c9c9c9,#7d7d7d)}
.clients .who{font-size:12px;letter-spacing:.4px}
.clients .role{font-size:11px;color:var(--red);margin:3px 0 12px}
.quote{display:flex;gap:10px;align-items:flex-start;font-size:11px;color:#444;line-height:1.45;padding:0 10px}
.quote b{font-size:28px;line-height:.8;font-family:'Roboto Slab',serif}
.quote p{flex:1}
.stars{color:#f0a500;font-size:12px;letter-spacing:2px;margin:12px 0 4px}
.clients .dots{padding:6px 0 0}
.view-more{text-align:center;padding:34px 0 40px}
.view-more .btn{font-size:10px;padding:7px 22px;font-weight:700}

/* blogs */
.blogs{padding:0 16px}
.blogs .head{display:flex;justify-content:space-between;align-items:center}
.blogs h2{font-size:20px;font-weight:500}
.blogs .arrows{color:#666;font-size:14px;letter-spacing:6px}
.blogs .intro{font-size:12px;color:#555;margin:4px 0 26px;width:60%}
.post{display:flex;gap:14px;margin-bottom:26px}
.post .thumb{width:130px;height:104px;flex:none}
.post .t1{background:linear-gradient(135deg,#4a4a4a,#9a8e86)}
.post .t2{background:linear-gradient(135deg,#6a8a5a,#c55a3a 55%,#3a5a8a)}
.post h4{font-size:12px;font-weight:700}
.post .meta{display:flex;justify-content:space-between;font-size:9px;margin:4px 0}
.post .meta span:first-child{color:var(--red)}
.post p{font-size:9.5px;color:#555;line-height:1.4}
.post .read{font-size:9px;color:#333;margin-top:3px}

/* brands */
.brands{padding-top:14px}
.brand-row{display:flex;align-items:center;justify-content:space-between;padding:22px 8px 0;font-size:13px;font-weight:700;color:#222}
.brand-row .arr{color:var(--red);font-size:12px}

/* newsletter */
.news{padding:48px 16px 0;text-align:center}
.news h3{font-size:19px;font-weight:500}
.news p{font-size:9px;color:#666;margin:4px 0 14px}
.news form{display:flex;height:22px}
.news .field{flex:1;border:1px solid var(--line);font-size:8px;color:#999;text-align:left;padding:6px 8px}
.news .send{background:var(--red);color:var(--white);font-size:8px;padding:6px 30px}

/* features */
.features{display:grid;grid-template-columns:1fr 1fr;gap:14px;padding:44px 14px 30px}
.feature{background:var(--panel);height:104px;display:flex;flex-direction:column;align-items:center;justify-content:center;gap:10px;font-size:12px}

/* footer */
.footer{background:var(--dark);color:var(--white);padding:56px 16px 20px}
.footer h4{font-size:15px;font-weight:500}
.footer .rule{height:1px;background:#444;margin:12px 0 14px}
.form-grid{display:grid;grid-template-columns:1fr 1fr;gap:6px;font-size:9px}
.form-grid div{background:#2a2a2d;padding:6px 8px}
.form-grid .msg{grid-column:1/3;height:52px}
.footer .send{text-align:center;margin:18px 0 14px}
.footer .send span{background:var(--red);font-size:8px;padding:4px 22px;border-radius:3px}
.footer .big{font-weight:900;color:var(--red);font-size:52px;line-height:1}
.footer .about{font-size:10.5px;line-height:1.4;margin:8px 0 12px}
.cards{display:flex;gap:8px}
.cards span{background:var(--white);color:#333;font-size:8px;font-weight:700;padding:5px 6px;width:44px;text-align:center}
.cols{display:grid;grid-template-columns:1fr 1.4fr;margin-top:38px;font-size:10px;line-height:1.5}
.cols h5{font-size:11px;font-weight:500;margin-bottom:10px}
.cols ul{list-style:disc;padding-left:14px}
.cols .addr div{display:flex;gap:6px;margin-bottom:3px}
.social{display:flex;gap:8px;margin:22px 0 20px}
.social i{width:22px;height:22px;border-radius:50%;background:var(--white);display:block}
.copy{border-top:1px solid #444;padding-top:12px;font-size:9.5px}
</style>
</head>
<body>
<div class="page">

  <header class="topbar">
    <svg width="16" height="12" viewBox="0 0 16 12"><path d="M0 1h16M0 6h16M0 11h16" stroke="#fff" stroke-width="2"/></svg>
    <div class="logo">Velmiro</div>
    <div class="icons">
      <svg width="13" height="13" viewBox="0 0 13 13"><circle cx="6.5" cy="4" r="3" fill="none" stroke="#fff" stroke-width="1.4"/><path d="M1 13c0-4 11-4 11 0" fill="none" stroke="#fff" stroke-width="1.4"/></svg>
      <svg width="14" height="13" viewBox="0 0 14 13"><path d="M7 12L1.5 6.5A3 3 0 017 2.5a3 3 0 015.5 4z" fill="none" stroke="#fff" stroke-width="1.4"/></svg>
      <svg width="14" height="13" viewBox="0 0 14 13"><path d="M1 1h2l2 8h7l1.5-6H4" fill="none" stroke="#fff" stroke-width="1.4"/><circle cx="6" cy="11.5" r="1.2" fill="#fff"/><circle cx="11" cy="11.5" r="1.2" fill="#fff"/></svg>
    </div>
  </header>

  <section class="hero">
    <div class="deal">50% OFF</div>
    <div class="sub">TUSENTALS SHOR</div>
    <span class="btn">Shop Now</span>
    <div class="photo" role="img" aria-label="Pair of brown leather lace-up shoes"></div>
  </section>
  <div class="dots"><i></i><i class="on"></i><i></i></div>

  <section class="cats">
    <div class="cat men" role="img" aria-label="Men's brown boots on a wooden floor">
      <span class="off">30% Off</span><h3>Shoes For Men</h3><span class="btn">Shop Now</span>
    </div>
    <div class="cat women" role="img" aria-label="Women's pink heels">
      <h3>Shoes For Women</h3><span class="off">30% Off</span><span class="btn" style="margin-top:8px">Shop Now</span>
    </div>
    <div class="cat kids" role="img" aria-label="Children's pink shoes">
      <span class="off">30% Off</span><h3>Shoes For Children</h3><span class="btn">Shop Now</span>
    </div>
  </section>

  <section class="popular">
    <h2 class="section-title">Popular Products</h2>
    <div class="tabs"><span class="on">Featured</span><b>|</b><span>Latest</span><b>|</b><span>Bestseller</span></div>
    <div class="grid">
      <div class="product"><div class="shot"><span role="img" aria-label="Pink and black sandal" style="background:#9a3a6a"></span></div>
        <div class="actions"><span class="btn btn-outline">Wish</span><span class="btn btn-solid">Buy</span></div>
        <div class="name">Boots - Greek White Finch</div><div class="price">850 kr</div></div>
      <div class="product"><div class="shot"><span role="img" aria-label="Tan leather sandal" style="background:#c89a6a"></span></div>
        <div class="name" style="margin-top:32px">Midsolle Slipper</div><div class="price">850 kr</div></div>
      <div class="product"><div class="shot"><span role="img" aria-label="Dark blue clog" style="background:#2a3a4a"></span></div>
        <div class="name">Cove Clouds</div><div class="price">390 kr</div></div>
      <div class="product"><div class="shot"><span role="img" aria-label="Black strappy sandal" style="background:#333"></span></div>
        <div class="name">Sledas</div><div class="price">599 kr</div></div>
      <div class="product"><div class="shot"><span role="img" aria-label="Navy running sneaker" style="background:#2c3552"></span></div>
        <div class="name">Nordpace</div><div class="price">890 kr</div></div>
      <div class="product"><div class="shot"><span role="img" aria-label="Blue canvas slip-on" style="background:#2a5aa0"></span></div>
        <div class="name">Toni</div><div class="price">380 kr</div></div>
    </div>
    <div class="more"><span class="btn btn-outline">View More</span></div>
  </section>

  <section class="arrived">
    <div>
      <h3>JUST ARRIVED</h3>
      <p>NEW SEASON SHOES COLLECTION</p>
      <div class="row"><span class="btn btn-outline">Shop Now</span><span class="btn btn-solid">Explore</span></div>
    </div>
    <div class="photo" role="img" aria-label="Two burgundy leather shoes"></div>
  </section>

  <section class="clients">
    <h2>Our Client Say</h2>
    <div class="avatar" role="img" aria-label="Client portrait"></div>
    <div class="who">ELIAS NORDIN</div>
    <div class="role">Creative Director</div>
    <div class="quote"><b>“</b><p>Lorem ipsum simply dummy text of the printing and typesetting industry. Lorem ipsum has been the text of the printing.</p><b>”</b></div>
    <div class="stars">★★★★★</div>
    <div class="dots"><i class="on"></i><i></i><i></i></div>
  </section>
  <div class="view-more"><span class="btn btn-solid">VIEW MORE</span></div>

  <section class="blogs">
    <div class="head"><h2>Blogs</h2><span class="arrows">‹ ›</span></div>
    <p class="intro">Lorem Ipsum is simply dummy text of the printing industry</p>
    <article class="post"><div class="thumb t1" role="img" aria-label="Sneakers on a dark floor"></div>
      <div><h4>The 10 Best Marnel Shoes</h4><div class="meta"><span>By Kara Lund</span><span>Mar 09, 2018</span></div>
      <p>Lorem Ipsum is simply dummy text of the printing and typesetting industry. Lorem Ipsum has been the industry's standard dummy text.</p><div class="read">Read More ⊕</div></div></article>
    <article class="post"><div class="thumb t2" role="img" aria-label="Colourful trail sneakers"></div>
      <div><h4>Joren x Marnel Vento Ridge Trail</h4><div class="meta"><span>By Kara Lund</span><span>Jan 09, 2018</span></div>
      <p>Lorem Ipsum is simply dummy text of the printing and typesetting industry. Lorem Ipsum has been the industry's standard dummy text.</p><div class="read">Read More ⊕</div></div></article>
    <div class="center"><span class="btn btn-outline" style="color:#333;border-color:#333">View More</span></div>
  </section>

  <section class="brands">
    <h2 class="section-title" style="font-size:24px;margin-top:16px">Brands</h2>
    <div class="brand-row"><span class="arr">‹</span><span>Stridex</span><span>Korvan</span><span>Tallo</span><span>Marnel</span><span class="arr">›</span></div>
  </section>

  <section class="news">
    <h3>Join The Newsletter</h3>
    <p>Sign up for our Newsletter</p>
    <form><div class="field">Email Here</div><div class="send">Subscribe</div></form>
  </section>

  <section class="features">
    <div class="feature"><svg width="30" height="22" viewBox="0 0 30 22"><rect x="1" y="3" width="17" height="12" fill="var(--red)"/><path d="M18 7h6l4 4v4H18z" fill="var(--red)"/><circle cx="7" cy="18" r="3" fill="var(--red)"/><circle cx="23" cy="18" r="3" fill="var(--red)"/></svg>Free Shipping</div>
    <div class="feature"><svg width="26" height="26" viewBox="0 0 26 26"><circle cx="13" cy="13" r="11" fill="none" stroke="var(--red)" stroke-width="3"/><text x="13" y="17" font-size="10" text-anchor="middle" fill="var(--red)" font-family="Roboto,sans-serif" font-weight="700">24</text></svg>24/7 Technical Support</div>
    <div class="feature"><svg width="26" height="26" viewBox="0 0 26 26"><circle cx="13" cy="13" r="10" fill="none" stroke="var(--red)" stroke-width="3"/><path d="M9 13h8M13 9v8" stroke="var(--red)" stroke-width="3"/></svg>Return And Exchanges</div>
    <div class="feature"><svg width="26" height="26" viewBox="0 0 26 26"><path d="M4 8h18l-2 16H6z" fill="var(--red)"/><path d="M9 8a4 4 0 018 0" fill="none" stroke="var(--red)" stroke-width="2"/></svg>Shopping Guide</div>
  </section>

  <footer class="footer">
    <h4>Quick Contact</h4>
    <div class="rule"></div>
    <div class="form-grid"><div>Name</div><div>Phone</div><div class="msg">Message</div></div>
    <div class="send"><span>Send</span></div>
    <div class="big">Velmiro</div>
    <p class="about">Lorem Ipsum is simply dummy text of the printing and typesetting industry. Has been the industry's standard print dummy....</p>
    <div class="cards"><span>Cardo</span><span>Payvo</span><span>Lumen</span><span>Orbit</span></div>
    <div class="cols">
      <div><h5>Quick Link</h5><ul><li>Home</li><li>About Us</li><li>Product</li><li>Brands</li><li>Blog</li><li>Contact</li></ul></div>
      <div class="addr"><h5>Address</h5>
        <div><span>⌖</span><span>Head office: Lindvägen 12, 114 27 Stockholm, Sweden</span></div>
        <div><span>✆</span><span>0800 214 563</span></div>
        <div><span>✉</span><span>info@velmiro.se</span></div>
      </div>
    </div>
    <div class="social"><i></i><i></i><i></i><i></i><i></i></div>
    <div class="copy">© 2018 All rights reserved | Terms &amp; Conditions | Privacy</div>
  </footer>
</div>
</body>
</html>
```